DOUBLE SIDED BROCHURE NEEDED TO PROMOTE DOCTOR

I need a double sided DL size (99mm x 210mm) brochure, promoting a doctor seeing patients in a new area.

I want something professional. I have included the relevant information. I would also like the Dr's picture somwhere in the brochure, with a professional background. I wish to print these tomorrow, so i will pick a winner within 14 hours of posting this ad.

I have included an example of a brochures design that I recently saw, and its definietly a good starting point.

Medical

```html
<!DOCTYPE html>
<html lang="en">
<head>
<meta charset="utf-8">
<title>Dr. Omar Haddad – Referral Brochure</title>
<link href="https://fonts.googleapis.com/css2?family=Poppins:wght@500;600&display=swap" rel="stylesheet">
<style>
  :root {
    --page-bg: #e9e9e9;
    --orange: #f5843d;
    --orange-light: #f7934e;
    --orange-deep: #f76a12;
    --olive: #b5b21a;
    --heart-red: #c8141c;
    --photo-sky: #8fb4dc;
    --photo-ground: #6c7780;
    --text: #ffffff;
  }
  * { box-sizing: border-box; margin: 0; padding: 0; }
  html, body { width: 1200px; height: 1200px; overflow: hidden; }
  body {
    background: var(--page-bg);
    font-family: "Poppins", sans-serif;
    color: var(--text);
    position: relative;
  }
  .panel {
    position: absolute;
    top: 166px;
    width: 400px;
    height: 868px;
    background: linear-gradient(180deg, var(--orange-light), var(--orange));
    overflow: hidden;
  }
  .panel--front { left: 170px; }
  .panel--back { left: 630px; }
  .panel__shape { position: absolute; inset: 0; }

  .hearts-art {
    position: absolute;
    left: 218px; top: 28px;
    width: 146px; height: 100px;
    border-radius: 50%;
    background: radial-gradient(circle at 50% 50%, var(--heart-red), rgba(200,20,28,0.15) 70%, transparent 72%);
  }
  .letter {
    position: absolute;
    left: 9px; right: 4px; top: 100px;
    font-weight: 600;
    font-size: 18.5px;
    line-height: 27.5px;
    letter-spacing: -0.3px;
  }
  .letter p + p { margin-top: 27px; }

  .contact {
    position: absolute;
    left: 8px; right: 4px; top: 517px;
    list-style: none;
    font-weight: 500;
    font-size: 22px;
    line-height: 30px;
  }
  .contact li { display: flex; align-items: flex-start; gap: 14px; }
  .contact li + li { margin-top: 30px; }
  .contact svg { flex: none; width: 38px; height: 40px; margin-top: 2px; }

  .surgeon-photo { position: absolute; inset: 0; }
  .profile {
    position: absolute;
    left: 19px; right: 6px; top: 370px;
    font-weight: 600;
    font-size: 18.5px;
    line-height: 27.5px;
    letter-spacing: -0.3px;
  }
  .profile ul { list-style: none; margin-top: 10px; }
  .profile .spaced { margin-top: 4px; }
</style>
</head>
<body>

  <section class="panel panel--front">
    <svg class="panel__shape" viewBox="0 0 400 868" aria-hidden="true">
      <defs>
        <linearGradient id="contactFill" x1="0" x2="1" y1="0" y2="0">
          <stop offset="0" stop-color="#f0873e"/>
          <stop offset="1" stop-color="#f96a10"/>
        </linearGradient>
      </defs>
      <path d="M0 458 Q200 440 400 568 L400 800 Q330 855 250 868 L0 868 Z" fill="url(#contactFill)"/>
      <path d="M230 468 Q340 500 400 572" fill="none" stroke="var(--olive)" stroke-width="4"/>
      <path d="M400 796 Q330 852 250 868" fill="none" stroke="var(--olive)" stroke-width="4"/>
    </svg>

    <div class="hearts-art" role="img" aria-label="Two glossy red hearts"></div>

    <div class="letter">
      <p>Dear Doctors,</p>
      <p>We are pleased to announce that Dr. Omar Haddad is now consulting in Coastvale, seeing public and private patients.</p>
      <p>Guaranteed appointment within two weeks, with patients having the option of surgery at Bayside Health Campus, Westbrook Hospital or St. Clare's Riverton.</p>
    </div>

    <ul class="contact">
      <li>
        <svg viewBox="0 0 38 40" aria-hidden="true"><path d="M17 2a12 12 0 0 0-12 12c0 9 12 24 12 24s12-15 12-24A12 12 0 0 0 17 2zm0 17a5 5 0 1 1 0-10 5 5 0 0 1 0 10z" fill="#fff"/></svg>
        <span>Coastvale Clinic:<br>24 Lakeside Drive<br>Coastvale WA 6000.</span>
      </li>
      <li>
        <svg viewBox="0 0 38 40" aria-hidden="true"><path d="M9 3l6 8-4 4c2 5 6 10 12 13l4-4 8 6-4 7C17 35 5 22 3 8z" fill="#fff"/></svg>
        <span>Phone: 1300 000 123</span>
      </li>
      <li>
        <svg viewBox="0 0 38 40" aria-hidden="true"><rect x="2" y="14" width="9" height="20" rx="2" fill="#fff"/><rect x="13" y="3" width="18" height="12" fill="#fff"/><rect x="12" y="16" width="24" height="18" rx="2" fill="#fff"/><rect x="16" y="20" width="16" height="3" fill="var(--orange)"/><rect x="16" y="26" width="16" height="3" fill="var(--orange)"/></svg>
        <span>Please send all referrals by fax to (08) 5550 0142.</span>
      </li>
    </ul>
  </section>

  <section class="panel panel--back">
    <svg class="surgeon-photo" viewBox="0 0 400 868" role="img" aria-label="Portrait of Dr. Omar Haddad in front of a modern hospital building">
      <defs>
        <linearGradient id="photoFill" x1="0" x2="0" y1="0" y2="1">
          <stop offset="0" stop-color="var(--photo-sky)"/>
          <stop offset="1" stop-color="var(--photo-ground)"/>
        </linearGradient>
      </defs>
      <path d="M0 0 L400 0 L400 320 Q260 300 120 310 Q40 316 0 300 Z" fill="var(--olive)"/>
      <path d="M0 112 Q140 10 400 6 L400 320 Q260 310 120 322 Q40 325 0 268 Z" fill="url(#photoFill)"/>
      <path d="M0 0 L400 0 L400 4 Q160 2 0 110 Z" fill="var(--orange-light)"/>
      <path d="M0 112 Q140 10 400 6" fill="none" stroke="var(--olive)" stroke-width="5"/>
      <path d="M0 268 Q40 325 120 322 Q260 310 400 320" fill="none" stroke="var(--olive)" stroke-width="7"/>
      <path d="M0 276 Q40 338 120 336 Q260 324 400 332 L400 320 Q260 310 120 322 Q40 325 0 268 Z" fill="var(--orange-light)"/>
    </svg>

    <div class="profile">
      <p>Dr. Haddad is a highly trained specialised surgeon, in all areas of Endocrine, Breast and General Surgery. Including:</p>
      <ul>
        <li>•Thyroid Surgery</li>
        <li>• Parathyroid surgery (including minimally invasive parathyroidectomy)</li>
        <li>• Breast Cancer Benign breast lesions</li>
      </ul>
      <p class="spaced">All areas of general surgery, such as;</p>
      <ul class="spaced">
        <li>•Gallbladder surgery</li>
        <li>•Hernia surgery</li>
        <li>•Haemorrhoids</li>
        <li>•Carpal Tunnel</li>
        <li>•Vasectomy etc etc...</li>
      </ul>
    </div>
  </section>

</body>
</html>
```